Design a modern, classy & professional business card for an online real estate agency, specializing in medium-luxury properties in Thailand and later in Singapore and UK.

Possible design ideas so far: (not essential)

- curved corner(s) to the card, white on front & turquoise on back or visa versa.

- front of card - clear and simple, company name in metallic grey/monochrome, logo graphic & company name on front in spot UV or embossed/debossed effect.

- back of card - large, close-cropped, 'ghost' patterns of the C-shaped curves of logo, or company name repeated on back of card in spot UV.

Target Market(s)

- young to middle-aged professionals mainly (but ideally should design should suit all)

- UK, US,EU,AUS & ASIAN mainly (but ideally should design should suit all countries)

Industry/Entity Type

Real Estate

Requirements
Must have
• THEME:
- Luxurious & Modern
- Clean & striking
- Unique & creative

INFO:
- Logo & company name on front
- Contact details on back:

Tobias Lindqvar
Managing Director

www.velmoraestates.example
www.velmoraestates-uk.example

Tel: 084-273-6190
email: tobias@velmoraestates.example

(contact details can be displayed in any order as suites design.)

Nice to have
• - curved corner(s) to the card, white on front & turquoise on back or visa versa.

Should not have
• - No generic images of properties, palm trees/coconut trees etc.

- No other other bold colors, except for main turquoise, grey, metallic white & black theme.

- No obvious business card templates

```html
<!DOCTYPE html>
<html lang="en">
<head>
<meta charset="utf-8">
<title>Velmora Estates — Business Card</title>
<link rel="stylesheet" href="https://fonts.googleapis.com/css2?family=Montserrat:ital,wght@0,400;0,500;0,700;1,400&display=swap">
<style>
  :root {
    --backdrop: #e9e9ea;
    --card-white: #ffffff;
    --turquoise: #6bbcb8;
    --turquoise-deep: #5aaeaa;
    --grey-text: #6a6a6a;
    --grey-mark: #e6e6e6;
    --edge-grey: #9a9a9c;
    --ink: #2f3a3a;
    --white: #ffffff;
  }
  * { box-sizing: border-box; margin: 0; padding: 0; }
  html, body {
    width: 1200px; height: 675px; overflow: hidden;
    background: var(--backdrop);
    font-family: "Montserrat", Arial, sans-serif;
  }
  .stage {
    position: relative; width: 1200px; height: 675px;
    display: flex; align-items: center; justify-content: center; gap: 60px;
  }
  .card {
    position: relative; width: 500px; height: 286px;
    border-radius: 6px; overflow: hidden;
    box-shadow: 0 6px 18px rgba(0,0,0,0.12);
  }
  .card--front { background: var(--card-white); }
  .card--back { background: linear-gradient(135deg, var(--turquoise-deep), var(--turquoise)); }

  .brand { position: absolute; display: flex; align-items: center; gap: 14px; }
  .brand__square { flex: none; }
  .brand__name {
    font-weight: 400; color: var(--grey-text); white-space: nowrap; letter-spacing: 0.5px;
  }
  .card--front .brand { left: 60px; top: 100px; }
  .card--front .brand__square { width: 86px; height: 86px; background: var(--turquoise); }
  .card--front .brand__name { font-size: 34px; }

  .card--back .brand { left: 34px; top: 62px; gap: 12px; }
  .card--back .brand__square { width: 62px; height: 62px; background: var(--grey-mark); }
  .card--back .brand__name { font-size: 24px; }

  .contacts {
    position: absolute; left: 284px; top: 136px; list-style: none;
    color: var(--white); font-size: 11.5px; line-height: 1;
  }
  .contacts li { display: flex; align-items: center; gap: 9px; height: 22px; }
  .contacts svg { width: 12px; height: 12px; flex: none; }

  .person { position: absolute; left: 40px; top: 220px; }
  .person__name { font-size: 15px; font-weight: 700; color: var(--white); }
  .person__role { font-size: 11.5px; font-style: italic; color: var(--ink); margin-top: 4px; }

  .edge-strip {
    position: absolute; left: 0; right: 0; bottom: 0; height: 8px; background: var(--edge-grey);
  }
</style>
</head>
<body>
<main class="stage">
  <section class="card card--front" aria-label="Card front">
    <div class="brand">
      <span class="brand__square"></span>
      <span class="brand__name">Velmora Estates</span>
    </div>
  </section>

  <section class="card card--back" aria-label="Card back">
    <div class="brand">
      <span class="brand__square"></span>
      <span class="brand__name">Velmora Estates</span>
    </div>

    <ul class="contacts">
      <li>
        <svg viewBox="0 0 12 12" aria-hidden="true"><path fill="#fff" d="M2.5 1h2l1 2.6-1.3 1a6 6 0 0 0 3.2 3.2l1-1.3L11 7.5v2A1.5 1.5 0 0 1 9.5 11 8.5 8.5 0 0 1 1 2.5 1.5 1.5 0 0 1 2.5 1z"/></svg>
        084-273-6190
      </li>
      <li>
        <svg viewBox="0 0 12 12" aria-hidden="true"><rect x="0.5" y="2" width="11" height="8" fill="#fff"/><path d="M0.5 2 6 6.5 11.5 2" fill="none" stroke="#5aaeaa" stroke-width="1"/></svg>
        tobias@velmoraestates.example
      </li>
      <li>
        <svg viewBox="0 0 12 12" aria-hidden="true"><circle cx="6" cy="6" r="5.5" fill="#fff"/><path d="M0.5 6h11M6 .5c-2.5 3-2.5 8 0 11M6 .5c2.5 3 2.5 8 0 11" fill="none" stroke="#5aaeaa" stroke-width="0.8"/></svg>
        www.velmoraestates.example
      </li>
      <li>
        <svg viewBox="0 0 12 12" aria-hidden="true"><circle cx="6" cy="6" r="5.5" fill="#fff"/><path d="M0.5 6h11M6 .5c-2.5 3-2.5 8 0 11M6 .5c2.5 3 2.5 8 0 11" fill="none" stroke="#5aaeaa" stroke-width="0.8"/></svg>
        www.velmoraestates-uk.example
      </li>
    </ul>

    <div class="person">
      <p class="person__name">Tobias Lindqvar</p>
      <p class="person__role">Managing Director</p>
    </div>

    <div class="edge-strip"></div>
  </section>
</main>
</body>
</html>
```